依頼詳細
現在、不動産業務にて空家・空地・相続させたお客様へお手紙と返信用ハガキをつけお送りしています。使用していますはがきデザインはワードで作成し、プリンターではがきに印刷しお手紙に添えてお送りしています。
返信いただくお客様に、
該当する内容に〇をつけていただき、送っていただいております。(2パターン使用中です)
お客様からの返信率はあまりない状況です。

※お客様の年齢層の幅も広いですし、相続対象者の方にもお送りしますので、お客様の中に はDMはがき自体を不快に思われる方もいらっしゃいますので、
デザインはシンプルなもので字体やバランスなどのご提案も含めお願いしたいです。
記載項目
裏面:ご回答書(ご所有の不動産について)、ご意見・ご要望、お客様のご住所・
お名前・ご連絡先
希望イメージ
シンプル 複雑
単色 カラフル
暗い 明るい
日常 高級
遊び心 厳粛
未来的 伝統的
女性的 男性的
希望する色
納品ファイル
• 高解像度JPG (.jpg)
• PNG形式 (.png)
補足説明
■ 選んだ理由

提案していただきありがとうございました。
見た瞬間から目を引かれるデザインで、柔らかい雰囲気がとても気に入りました。

■ 提案者全員のお礼・コメント

素晴らしいデザインでした!
ありがとうございました。

```html
<!DOCTYPE html>
<html lang="ja">
<head>
<meta charset="utf-8">
<title>ご回答書</title>
<link href="https://fonts.googleapis.com/css2?family=M+PLUS+Rounded+1c:wght@500;700;800&family=Noto+Sans+JP:wght@400;500&display=swap" rel="stylesheet">
<style>
  :root{
    --green:#3ba47f;
    --green-soft:#5fb795;
    --cream:#fdf5ec;
    --ink:#3d3d3d;
    --line:#9a9a9a;
    --white:#ffffff;
  }
  *{margin:0;padding:0;box-sizing:border-box;}
  html,body{width:813px;height:1200px;overflow:hidden;background:var(--cream);}
  .card{position:relative;width:813px;height:1200px;background:var(--cream);color:var(--ink);
    font-family:"Noto Sans JP",sans-serif;}
  .header-band{position:absolute;left:0;top:0;width:813px;height:82px;background:var(--green);
    display:flex;align-items:center;padding-left:30px;}
  .header-title{font-family:"M PLUS Rounded 1c",sans-serif;font-weight:800;font-size:35px;color:var(--white);letter-spacing:1px;}
  .intro{position:absolute;left:32px;top:108px;width:760px;font-size:21.5px;line-height:35px;letter-spacing:0.3px;}
  .question{position:absolute;left:32px;font-size:22px;letter-spacing:0.3px;}
  .q1{top:250px;}
  .q2{top:506px;}
  .tick{color:var(--green);font-weight:500;}
  .choices{position:absolute;left:66px;top:306px;width:700px;display:grid;grid-template-columns:344px 344px;row-gap:21px;}
  .choice{display:flex;align-items:center;font-size:21.5px;height:28px;}
  .choice-box{width:24px;height:24px;border:2.5px solid var(--green);background:var(--white);margin-right:18px;flex:none;}
  .choice-wide{grid-column:1 / span 2;}
  .comment-box{position:absolute;left:73px;top:560px;width:664px;height:212px;border:3px solid var(--green);
    border-radius:30px;background:var(--white);}
  .contact-table{position:absolute;left:49px;top:786px;width:715px;border-collapse:collapse;background:var(--white);}
  .contact-table th,.contact-table td{border:1.5px solid var(--line);}
  .contact-table th{width:141px;font-weight:500;font-size:22px;text-align:center;}
  .contact-table td{font-size:22px;vertical-align:top;padding:6px 10px;}
  .row-kana th{font-size:13px;height:27px;}
  .row-name th{height:60px;}
  .row-address th{height:116px;}
  .row-phone th{height:95px;}
  .footer-band{position:absolute;left:0;top:1090px;width:813px;height:110px;background:var(--green);}
  .footer-motif{position:absolute;left:50px;top:14px;width:60px;height:82px;border-radius:30px 30px 8px 8px;
    background:linear-gradient(180deg,var(--green-soft),var(--green));}
  .footer-message{position:absolute;left:0;top:12px;width:813px;text-align:center;
    font-family:"M PLUS Rounded 1c",sans-serif;font-weight:700;font-size:30px;line-height:43px;color:var(--white);letter-spacing:1px;}
</style>
</head>
<body>
<main class="card">
  <header class="header-band">
    <h1 class="header-title">回答書のご記入にご協力をお願いします。</h1>
  </header>

  <p class="intro">ご所有の不動産について、ご意見・ご要望を是非お聞かせください。<br>下記ご記入の上、弊社へ郵送またはご持参いただくか Fax にて、こちら<br>の回答書のご返送をお願いいたします。</p>

  <p class="question q1">①下記より該当する項目に<span class="tick">✓</span>印をお付けください。</p>
  <ul class="choices">
    <li class="choice"><span class="choice-box"></span>売却してもよい</li>
    <li class="choice"><span class="choice-box"></span>売却するつもりはない</li>
    <li class="choice"><span class="choice-box"></span>どちらとも決めていない</li>
    <li class="choice"><span class="choice-box"></span>不動産の価値を知りたい</li>
    <li class="choice"><span class="choice-box"></span>当分様子をみて決める</li>
    <li class="choice"><span class="choice-box"></span>不動産の活用を考えている</li>
    <li class="choice choice-wide"><span class="choice-box"></span>将来自分（子供）が家を建てて住む予定</li>
  </ul>

  <p class="question q2">②ご意見・ご要望をご記入ください。</p>
  <div class="comment-box"></div>

  <table class="contact-table">
    <tr class="row-kana"><th>フリガナ</th><td></td></tr>
    <tr class="row-name"><th>お名前</th><td></td></tr>
    <tr class="row-address"><th>ご住所</th><td>〒</td></tr>
    <tr class="row-phone"><th>ご連絡先</th><td></td></tr>
  </table>

  <footer class="footer-band">
    <div class="footer-motif" role="img" aria-label="チューリップの線画イラスト"></div>
    <p class="footer-message">ご回答ありがとうございました。<br>今後ともよろしくお願いいたします。</p>
  </footer>
</main>
</body>
</html>
```